wealth management firm, professional group, new model

we have a logo that works but we need a card, white background using our colors...clean look

our tag line if can be used in

Steady Counsel From Start to Legacy

```html
<!DOCTYPE html>
<html lang="en">
<head>
<meta charset="utf-8">
<title>Arvello Capital Advisors – Business Card</title>
<link rel="stylesheet" href="https://fonts.googleapis.com/css2?family=Montserrat:wght@400;600;700&display=swap">
<style>
  :root {
    --navy: #1c3560;
    --navy-ink: #1f3a66;
    --navy-soft: #8fa0bd;
    --paper: #ffffff;
    --stage: #e9e7e3;
    --ink: #2b2b2b;
    --tagline: #d9deea;
  }
  * { margin: 0; padding: 0; box-sizing: border-box; }
  html, body {
    width: 1200px; height: 747px; overflow: hidden;
    background: var(--stage);
    font-family: "Montserrat", sans-serif;
  }
  .canvas {
    width: 1200px; height: 747px;
    display: flex; align-items: center; justify-content: center; gap: 80px;
  }
  .card {
    width: 330px; height: 578px;
    position: relative;
    box-shadow: 0 6px 18px rgba(0,0,0,0.12);
  }
  .card--front { background: var(--navy); }
  .card--back { background: var(--paper); }

  .wordmark {
    position: absolute; left: 0; right: 0;
    text-align: center;
    white-space: nowrap;
  }
  .wordmark__name {
    display: block;
    font-weight: 400;
    font-size: 34px;
    letter-spacing: 0.32em;
    padding-left: 0.32em;
  }
  .wordmark__sub {
    display: block;
    margin-top: 8px;
    font-weight: 400;
    font-size: 12px;
    letter-spacing: 0.26em;
    padding-left: 0.26em;
  }
  .card--front .wordmark { top: 180px; color: var(--navy-soft); }
  .card--back .wordmark { top: 66px; color: var(--navy-ink); }

  .tagline {
    position: absolute; left: 0; right: 0; top: 368px;
    text-align: center;
    white-space: nowrap;
    color: var(--tagline);
    font-size: 8px;
    letter-spacing: 0.2em;
    text-transform: uppercase;
  }

  .contact {
    position: absolute; left: 40px; top: 262px;
    color: var(--ink);
    font-size: 16px;
    line-height: 1.3;
    white-space: nowrap;
  }
  .contact__name {
    color: var(--navy-ink);
    font-weight: 700;
    text-transform: uppercase;
  }
  .contact__role { color: #3a3a3a; }
  .contact__address { margin-top: 18px; }
  .contact__lines { margin-top: 6px; }
</style>
</head>
<body>
  <main class="canvas">
    <section class="card card--front" aria-label="Card front">
      <div class="wordmark">
        <span class="wordmark__name">ARVELLO</span>
        <span class="wordmark__sub">CAPITAL ADVISORS</span>
      </div>
      <p class="tagline">Steady Counsel From Start to Legacy</p>
    </section>

    <section class="card card--back" aria-label="Card back">
      <div class="wordmark">
        <span class="wordmark__name">ARVELLO</span>
        <span class="wordmark__sub">CAPITAL ADVISORS</span>
      </div>
      <div class="contact">
        <p class="contact__name">Marco Valenti</p>
        <p class="contact__role">Brand Manager</p>
        <p class="contact__address">Via Corsico 14<br>20144 Milano, Italy</p>
        <p class="contact__lines">+39.340.512.7781<br>info@arvellomail.com<br>www.arvelloweb.com</p>
      </div>
    </section>
  </main>
</body>
</html>
```